WRM Marketing Postcard

Design a 2 Sided marketing postcard for our Real estate management caompany. Looking for a professional yet fresh look that will be printed on a 6"x9" glossy flier

Contact information is www.wexleymanagement.com wexleymanagement@inboxvane.com and 312-555-0187

WE are targeting small condo and town home properties to take on their administrative responsibilities of management

```html
<!DOCTYPE html>
<html lang="en">
<head>
<meta charset="utf-8">
<title>WRM Marketing Postcard</title>
<link rel="stylesheet" href="https://fonts.googleapis.com/css2?family=Open+Sans:wght@400;600;700;800&display=swap">
<style>
  :root {
    --bg: #5a5a5c;
    --card: #4b4c4f;
    --card-dark: #3d3e41;
    --red: #ec1c24;
    --red-dark: #b5121a;
    --white: #ffffff;
    --ink: #3a3a3c;
  }
  * { box-sizing: border-box; margin: 0; padding: 0; }
  html, body { width: 960px; height: 1200px; overflow: hidden; }
  body {
    background: var(--bg);
    font-family: "Open Sans", Arial, sans-serif;
    color: var(--white);
    position: relative;
  }
  .tick-defs { position: absolute; width: 0; height: 0; }
  .card {
    position: absolute;
    left: 94px;
    width: 778px;
    height: 518px;
    background: linear-gradient(180deg, var(--card) 0%, var(--card-dark) 100%);
    overflow: hidden;
  }
  .card--front { top: 70px; }
  .card--back { top: 617px; }

  /* front */
  .front-visual { position: absolute; left: 0; top: 0; }
  .front-title {
    position: absolute; left: 31px; top: 42px;
    font-weight: 800; font-size: 27px; line-height: 34px; letter-spacing: 0.2px;
    white-space: nowrap;
  }
  .benefits { position: absolute; left: 34px; top: 126px; width: 370px; list-style: none; }
  .benefits li {
    position: relative; padding-left: 20px;
    font-size: 13.9px; line-height: 19.5px; margin-bottom: 10px;
    white-space: nowrap;
  }
  .benefits li strong { font-weight: 700; }
  .tick { position: absolute; left: 0; top: 4px; width: 13px; height: 12px; }
  .front-band {
    position: absolute; left: 0; top: 421px; width: 404px; height: 76px;
    background: var(--red); padding: 10px 0 0 31px;
  }
  .call { font-weight: 800; font-size: 19px; line-height: 28px; }
  .call .phone { font-size: 27px; letter-spacing: 0.3px; }
  .web { font-size: 20px; line-height: 26px; }
  .web strong { font-weight: 700; }
  .price-badge {
    position: absolute; left: 396px; top: 338px; width: 144px; height: 144px;
    border-radius: 50%; background: var(--white);
    text-align: center; color: var(--ink);
    font-weight: 800; padding-top: 22px;
  }
  .price-badge .lead { font-size: 18px; line-height: 20px; }
  .price-badge .amount { color: var(--red); font-size: 28px; line-height: 28px; }
  .price-badge .amount small { font-size: 18px; }
  .price-badge .per { color: var(--red); font-size: 16px; line-height: 18px; }

  /* back */
  .back-title {
    position: absolute; left: 0; right: 0; top: 24px; text-align: center;
    font-weight: 800; font-size: 27.5px; letter-spacing: 0.3px;
  }
  .back-strap {
    position: absolute; left: 45px; top: 58px; width: 687px; height: 34px;
    background: var(--red); text-align: center;
    font-weight: 600; font-size: 14.5px; line-height: 34px;
  }
  .col { position: absolute; top: 108px; }
  .col--left { left: 50px; width: 305px; }
  .col--right { left: 402px; width: 340px; }
  .col h3 { font-weight: 800; font-size: 17.5px; line-height: 24px; margin-bottom: 6px; }
  .col h3.gap { margin-top: 6px; margin-bottom: 4px; }
  .points { list-style: none; }
  .points li {
    position: relative; padding-left: 13px;
    font-size: 13.5px; line-height: 18.5px; margin-bottom: 10px; color: #f1f1f1;
  }
  .points li .tick { width: 9px; height: 8px; top: 4px; }
  .points--tight li { line-height: 15px; margin-bottom: 11px; }
  .back-band {
    position: absolute; left: 0; bottom: 8px; width: 100%; height: 75px;
    background: var(--red); text-align: center; padding-top: 7px;
  }
  .back-band .call { font-size: 26px; line-height: 36px; }
  .back-band .call .phone { font-size: 37px; }
  .back-band .web { font-size: 19.5px; line-height: 24px; }
</style>
</head>
<body>
<svg class="tick-defs" aria-hidden="true">
  <symbol id="tick" viewBox="0 0 13 12">
    <path d="M1 6.5 L4.8 10.5 L12 1.5" fill="none" stroke="#ec1c24" stroke-width="2.2" stroke-linecap="round" stroke-linejoin="round"/>
  </symbol>
</svg>

<section class="card card--front">
  <svg class="front-visual" width="778" height="518" viewBox="0 0 778 518">
    <defs>
      <linearGradient id="photoTone" x1="0" y1="0" x2="0" y2="1">
        <stop offset="0" stop-color="#c9d7e3"/>
        <stop offset="0.55" stop-color="#e6ebef"/>
        <stop offset="0.9" stop-color="#b9b9bb"/>
        <stop offset="1" stop-color="#8fbf5a"/>
      </linearGradient>
    </defs>
    <circle cx="712" cy="272" r="289" fill="var(--red)"/>
    <circle cx="718" cy="272" r="278" fill="url(#photoTone)" role="img" aria-label="Photo of a smiling property manager in a grey suit holding out keys and a blue folder, in front of faint building blueprints"/>
    <ellipse cx="468" cy="487" rx="52" ry="6" fill="var(--red-dark)"/>
  </svg>

  <h1 class="front-title">WEXLEY RESIDENTIAL<br>MANAGEMENT LLC (“WRM”)</h1>
  <ul class="benefits">
    <li><svg class="tick"><use href="#tick"/></svg>Cost effective property management solution<br>for 3-10 unit buildings</li>
    <li><svg class="tick"><use href="#tick"/></svg>Utilize our economies of scale to reduce costs across<br>existing services (trash, insurance, maintenance, etc)</li>
    <li><svg class="tick"><use href="#tick"/></svg>liminate the unfair burden placed on a few owners<br>to do all the work while others <strong>FREE-RIDE</strong></li>
    <li><svg class="tick"><use href="#tick"/></svg>Improve communication amongst all owners and<br>board members</li>
    <li><svg class="tick"><use href="#tick"/></svg>The association’s board of directors maintain all<br>decision-making power</li>
    <li><svg class="tick"><use href="#tick"/></svg>Utilize our vetted service providers for prompt<br>job completion and fair pricing</li>
  </ul>

  <div class="front-band">
    <p class="call">CALL US TODAY <span class="phone">312-555-0187</span></p>
    <p class="web">www.<strong>wexleymanagement</strong>.com</p>
  </div>

  <div class="price-badge">
    <p class="lead">PRICES<br>STARTING<br>AS LOW AS</p>
    <p class="amount">$100<small>/</small></p>
    <p class="per">MONTH</p>
  </div>
</section>

<section class="card card--back">
  <h2 class="back-title">WEXLEY RESIDENTIAL MANAGEMENT LLC (“WRM”)</h2>
  <p class="back-strap">Improve compliance, reporting, and communication amongst all owners and board member</p>

  <div class="col col--left">
    <h3>WHO WE ARE:</h3>
    <ul class="points">
      <li><svg class="tick"><use href="#tick"/></svg>A professional services organization with a focus on small (3-10 unit) residential buildings</li>
      <li><svg class="tick"><use href="#tick"/></svg>Over 30 years of combined experience in real estate and property management</li>
      <li><svg class="tick"><use href="#tick"/></svg>Professional, courteous, timely service that is technologically driven</li>
    </ul>
    <h3 class="gap">WHY USE WRM?</h3>
    <ul class="points points--tight">
      <li><svg class="tick"><use href="#tick"/></svg>Owners are rarely suited to manage associations and the burden often falls unfairly on one or two individuals to do all the work</li>
      <li><svg class="tick"><use href="#tick"/></svg>Low monthly fees tailored to your needs</li>
      <li><svg class="tick"><use href="#tick"/></svg>The association’s board of directors maintains control of all decision making</li>
    </ul>
  </div>

  <div class="col col--right">
    <h3>WHAT WE DO:</h3>
    <ul class="points">
      <li><svg class="tick"><use href="#tick"/></svg>Remove the administrative burden of managing small residential buildings</li>
      <li><svg class="tick"><use href="#tick"/></svg>Utilize economies of scale to reduce expenses for all owners across a wide variety of service providers</li>
      <li><svg class="tick"><use href="#tick"/></svg>Collect all assessments and pay all bills</li>
      <li><svg class="tick"><use href="#tick"/></svg>Provide monthly accounting reconciliation and reporting</li>
      <li><svg class="tick"><use href="#tick"/></svg>Issue 1099s to all contractors as required by law</li>
      <li><svg class="tick"><use href="#tick"/></svg>Prepare year-end financial statement</li>
      <li><svg class="tick"><use href="#tick"/></svg>Lender and legal HOA documents for mortgage companies and sales</li>
    </ul>
  </div>

  <div class="back-band">
    <p class="call">CALL US TODAY <span class="phone">312-555-0187</span></p>
    <p class="web">www.<strong>wexleymanagement</strong>.com | wexleymanagement@inboxvane.com</p>
  </div>
</section>
</body>
</html>
```